New Business Card Design Project

Make a kick ass business card for The Otter Tea Mug, using the designs. I also might like the 2nd place design logo on the back? Maybe all black with that? Not sure. Also, I'm cool with it being on metal, plastic, glass? or whatever for the business card. Maybe shaped like a shark? Let me know what else you need? Would like designs in the next day or so. Thank you.
Target Market(s)
Anyone that is cool
Contact Information for Business Card
Name: Dorian Fenwick
Phone: 317.594.8126
inventor/creator/entrepreneur/owner
www.theottertyeamug.example
social media links
https://www.facebook.com/theottertyeamug
https://twitter.com/otter_brew
https://www.instagram.com/theottertyeamug/
I'll get the Pinterest one soon
Colors
Designer to choose colors to be used in the design.
Requirements
Must have
- The Otter Tea Mug
- www.theottertyeamug.example
- social media tags?
- My logos and picture/photo of wine glass
Nice to have
- Maybe shaped like a wine glass or shark
- I'll let you decide but my same colors from my website would be nice

```html
<!DOCTYPE html>
<html lang="en">
<head>
<meta charset="utf-8">
<title>The Otter Tea Mug — Business Card</title>
<link rel="stylesheet" href="https://fonts.googleapis.com/css2?family=Jost:wght@300;400;600&display=swap">
<style>
  :root {
    --page-bg: #e9e9ea;
    --front-light: #a4a5a8;
    --front-dark: #6c6d70;
    --front-ink: #2f3033;
    --card-white: #ffffff;
    --accent-red: #b3383e;
    --text-gray: #7d7d80;
    --rule-gray: #9a9a9d;
    --icon-gray: #8f9094;
  }
  * { box-sizing: border-box; margin: 0; padding: 0; }
  html, body {
    width: 1200px; height: 900px; overflow: hidden;
    background: var(--page-bg);
    font-family: "Jost", sans-serif;
  }
  .sheet {
    width: 1200px; height: 900px;
    display: flex; flex-direction: column; align-items: center;
    justify-content: center; gap: 24px;
  }
  .card {
    width: 680px; height: 389px; position: relative;
    box-shadow: 0 6px 18px rgba(0,0,0,0.18);
  }
  .card--front {
    background: linear-gradient(135deg, var(--front-dark) 0%, var(--front-light) 50%, var(--front-dark) 100%);
    display: flex; align-items: center; justify-content: center;
  }
  .front-name {
    display: flex; align-items: center; gap: 14px;
    font-weight: 400; font-size: 36px; letter-spacing: 1px;
    color: var(--front-ink);
  }
  .brand-dot {
    width: 14px; height: 14px; border-radius: 50%;
    background: var(--front-ink); flex: none;
  }
  .card--back {
    background: var(--card-white);
    display: flex; align-items: center;
  }
  .back-brand {
    width: 50%; display: flex; justify-content: center; align-items: center;
  }
  .back-name {
    display: flex; align-items: center; gap: 10px;
    font-weight: 400; font-size: 26px; color: var(--accent-red);
    letter-spacing: 0.5px; margin-top: 40px;
  }
  .back-name .brand-dot { width: 10px; height: 10px; background: var(--accent-red); }
  .divider {
    width: 1px; height: 184px; background: var(--rule-gray);
  }
  .contact {
    padding-left: 24px; color: var(--text-gray);
    font-weight: 300; font-size: 14px; line-height: 1.45;
  }
  .contact__name {
    font-weight: 600; font-size: 20px; color: var(--accent-red);
    letter-spacing: 0.3px; line-height: 1.2;
  }
  .contact__role { margin-bottom: 4px; }
  .contact__row { display: flex; align-items: center; gap: 7px; }
  .contact__row svg { flex: none; }
  .contact__socials { margin-top: 8px; }
  .social-mark {
    width: 10px; height: 10px; background: var(--icon-gray);
    border-radius: 2px; flex: none;
  }
</style>
</head>
<body>
<main class="sheet">
  <section class="card card--front" aria-label="Card front">
    <p class="front-name"><span class="brand-dot"></span>The Otter Tea Mug</p>
  </section>

  <section class="card card--back" aria-label="Card back">
    <div class="back-brand">
      <p class="back-name"><span class="brand-dot"></span>The Otter Tea Mug</p>
    </div>
    <div class="divider"></div>
    <div class="contact">
      <p class="contact__name">Dorian Fenwick</p>
      <p class="contact__role">inventor/creator/entrepreneur/owner</p>
      <p class="contact__row">
        <svg width="12" height="12" viewBox="0 0 24 24" aria-hidden="true"><path d="M6.6 10.8a15 15 0 0 0 6.6 6.6l2.2-2.2a1 1 0 0 1 1-.25 11.4 11.4 0 0 0 3.6.57 1 1 0 0 1 1 1V20a1 1 0 0 1-1 1A17 17 0 0 1 3 4a1 1 0 0 1 1-1h3.5a1 1 0 0 1 1 1c0 1.25.2 2.45.57 3.6a1 1 0 0 1-.25 1z" fill="none" stroke="#b3383e" stroke-width="2"/></svg>
        317.594.8126
      </p>
      <p class="contact__row">
        <svg width="12" height="12" viewBox="0 0 24 24" aria-hidden="true"><circle cx="12" cy="12" r="9" fill="none" stroke="#b3383e" stroke-width="2"/><path d="M3 12h18M12 3c3 3 3 15 0 18M12 3c-3 3-3 15 0 18" fill="none" stroke="#b3383e" stroke-width="1.5"/></svg>
        www.theottertyeamug.example
      </p>
      <div class="contact__socials">
        <p class="contact__row"><span class="social-mark"></span>theottertyeamug</p>
        <p class="contact__row"><span class="social-mark"></span>otter_brew</p>
        <p class="contact__row"><span class="social-mark"></span>theottertyeamug</p>
        <p class="contact__row"><span class="social-mark"></span>theottertyeamug</p>
      </div>
    </div>
  </section>
</main>
</body>
</html>
```